Quorvane Learning App for Children with Dyslexia

Project Description:

We are seeking a talented UI/UX designer to create engaging and intuitive designs for Quorvane, an innovative educational app designed to help children learn letters and words through a multisensory learning approach. The app aims to be particularly helpful for children with dyslexia, providing a supportive and interactive learning environment.

Key App Features & Design Requirements:

Account Creation Screen: Design a welcoming and straightforward sign-up page that allows users to register with their email or continue with Brindlewave. The design should be clean, focusing on user-friendliness and accessibility, adhering to our terms of service and privacy policy.

Main Screen Design: The main screen should allocate at least 4/6 of its height to the interactive drawing area. It needs to display word prompts in both correct and scrambled orders and include options to "Show all Words," "Play all words," and a search function. The interface should be vibrant, engaging, and easy to navigate for children.

Profile Section: Create a user-friendly profile page that allows users to edit their profile image, name, username, email, links, and bio. The design should be clean and encourage user engagement.

QuorTally Page: This section will display the user's learning progress, including rankings, a learning curve, and recently learned words. It should visually represent progress in a motivating and understandable way, suitable for a younger audience.

Visual and Auditory Feedback Implementation: Incorporate elements that support visual and auditory feedback, using dyslexia-friendly formats. This includes choosing appropriate colors, fonts, and auditory cues.

Accessibility and Customization Settings: Designs should include settings for adjusting visual contrast, font size, and the word list to accommodate individual preferences and needs.

Feel free to add more interactions and/or pages.

Design preferences:

Color Scheme: Use a bright, inviting color palette that stimulates learning and engagement without overwhelming the users.
Font Selection: Opt for fonts that are readable and accessible, particularly for users with dyslexia.
Icons and Graphics: Design custom icons and graphics that are cohesive with the app's theme and purpose. Illustrations should be simple, relatable, and supportive of the learning process.

Target Market(s)

Educational

Industry/Entity Type

Educational

Colors
0054AA
0677BA
7BADD7
CADEEF
E8F1F8
0094D4
00A9DD
6FCCEA
C7EBF8
E9F6FB

Requirements
Must have
• Educational app, a writing area, scoring and account management
Nice to have
• Statistics, Ranking Page, Settings and some nice visual features

```html
<!DOCTYPE html>
<html lang="en">
<head>
<meta charset="utf-8">
<title>Quorvane – App Screens</title>
<link rel="stylesheet" href="https://fonts.googleapis.com/css2?family=Inter:wght@400;500;600;700;800&display=swap">
<style>
  :root {
    --brand-blue: #0567f5;
    --brand-blue-deep: #0358e0;
    --action-green: #00b853;
    --chip-blue: #cfe1fb;
    --surface: #eef1f6;
    --field: #edf0f5;
    --ink: #111418;
    --ink-soft: #3a3f47;
    --muted: #8a9099;
    --white: #ffffff;
    --gold: #f5b400;
  }
  * { box-sizing: border-box; margin: 0; padding: 0; }
  html, body { width: 1200px; height: 811px; overflow: hidden; background: var(--white); }
  body { font-family: "Inter", sans-serif; color: var(--ink); position: relative; }

  .screen {
    position: absolute; top: 147px; width: 234px; height: 508px;
    border-radius: 22px; overflow: hidden;
  }
  .screen--signup { left: 71px; background: linear-gradient(160deg, #0a66f6 0%, #0570f5 100%); color: var(--white); }
  .screen--main { left: 347px; background: var(--white); }
  .screen--profile { left: 618px; background: var(--surface); }
  .screen--stats { left: 895px; background: var(--surface); }

  .abs { position: absolute; }
  .center-x { left: 0; right: 0; text-align: center; }

  /* Sign up */
  .brand-title { top: 98px; font-size: 27px; font-weight: 800; letter-spacing: 0.5px; }
  .brand-tagline { top: 135px; font-size: 10.5px; font-weight: 500; }
  .signup-heading { top: 224px; font-size: 10.5px; font-weight: 600; }
  .signup-sub { top: 240px; font-size: 7.8px; }
  .pill {
    position: absolute; left: 15px; width: 204px; height: 33px; border-radius: 17px;
    display: flex; align-items: center; justify-content: center; font-size: 10px;
  }
  .email-field { top: 272px; background: var(--field); color: var(--muted); box-shadow: 0 3px 8px rgba(0,0,0,0.12); }
  .continue-btn { top: 315px; background: var(--action-green); color: var(--white); font-weight: 600; font-size: 10.5px; box-shadow: 0 3px 8px rgba(0,0,0,0.15); }
  .divider { top: 363px; left: 18px; width: 198px; display: flex; align-items: center; gap: 6px; font-size: 7.5px; }
  .divider::before, .divider::after { content: ""; flex: 1; height: 1px; background: rgba(255,255,255,0.25); }
  .provider-btn { top: 389px; background: var(--white); color: var(--ink); font-size: 8.6px; font-weight: 500; gap: 16px; box-shadow: 0 3px 8px rgba(0,0,0,0.12); }
  .provider-dot { width: 15px; height: 15px; border-radius: 50%; background: var(--brand-blue); }
  .legal { top: 468px; font-size: 7.5px; line-height: 10px; }
  .legal strong { font-weight: 700; }

  /* Headers */
  .header-title { top: 33px; font-size: 9.5px; font-weight: 700; color: var(--white); }
  .icon-back { left: 12px; top: 30px; }

  /* Main screen */
  .main-hero { left: 0; top: 0; width: 234px; height: 312px; background: var(--brand-blue); border-radius: 0 0 22px 22px; }
  .menu-icon { left: 10px; top: 34px; }
  .points-pill {
    left: 171px; top: 30px; width: 55px; height: 19px; border-radius: 10px; background: var(--white);
    display: flex; align-items: center; justify-content: center; gap: 4px; font-size: 7.6px; font-weight: 600;
  }
  .coin { width: 5px; height: 7px; border-radius: 2px; background: var(--gold); }
  .draw-pad { left: 7px; top: 65px; width: 220px; height: 237px; border-radius: 24px; background: var(--field); }
  .pen-icon { right: 10px; bottom: 12px; }
  .mode-toggle {
    left: 13px; top: 320px; width: 207px; height: 26px; border-radius: 13px; border: 1px solid #cfd3d9;
    display: flex; font-size: 8.6px; font-weight: 500;
  }
  .mode-toggle span { flex: 1; display: flex; align-items: center; justify-content: center; border-radius: 13px; color: var(--ink-soft); }
  .mode-toggle .is-active { background: var(--action-green); color: var(--white); margin: -1px; }
  .chip {
    position: absolute; width: 65px; height: 30px; border-radius: 8px; background: var(--chip-blue);
    display: flex; align-items: center; justify-content: center; font-size: 10px; font-weight: 500;
  }
  .dark-btn {
    position: absolute; background: var(--ink); color: var(--white); border-radius: 13px;
    display: flex; align-items: center; justify-content: center; font-weight: 500;
  }
  .result-btn { left: 58px; top: 467px; width: 122px; height: 26px; font-size: 8.6px; }

  /* Profile */
  .profile-band { left: 0; top: 0; }
  .avatar-large { left: 78px; top: 58px; width: 78px; height: 78px; border-radius: 50%; background: radial-gradient(circle at 45% 40%, #d9a27c 0%, #b77d56 40%, #7f8a92 100%); }
  .edit-btn { left: 73px; top: 146px; width: 85px; height: 20px; font-size: 7.4px; border-radius: 10px; }
  .field-row {
    position: absolute; left: 18px; width: 199px; height: 33px; border-radius: 6px; background: var(--white);
    display: flex; align-items: center; padding: 0 10px 0 16px; font-size: 8.4px; box-shadow: 0 2px 6px rgba(20,40,80,0.06);
  }
  .field-row .label { flex: 1; color: var(--ink-soft); font-weight: 500; }
  .field-row .value { color: var(--brand-blue); font-weight: 600; margin-right: 8px; }
  .add-link {
    position: absolute; left: 18px; top: 434px; width: 199px; height: 33px; border-radius: 6px; border: 1.2px solid var(--brand-blue);
    display: flex; align-items: center; justify-content: center; gap: 14px; font-size: 8.6px; font-weight: 600; color: var(--brand-blue);
  }

  /* Stats */
  .stats-header { left: 0; top: 0; width: 234px; height: 58px; background: var(--brand-blue); }
  .stats-title { top: 33px; font-size: 7.8px; font-weight: 600; color: var(--white); }
  .avatar-small { left: 194px; top: 26px; width: 26px; height: 26px; border-radius: 50%; background: radial-gradient(circle at 45% 40%, #d9a27c 0%, #b77d56 45%, #8c9298 100%); }
  .tab {
    position: absolute; top: 73px; height: 18px; border-radius: 9px; background: #c9d3e3;
    display: flex; align-items: center; justify-content: center; font-size: 7.2px; font-weight: 500; color: var(--ink);
  }
  .tab.is-active { background: var(--brand-blue); color: var(--white); }
  .rank-card {
    position: absolute; top: 107px; height: 65px; border-radius: 8px; border: 1px solid var(--brand-blue); background: var(--white);
  }
  .rank-card .rank-label { position: absolute; left: 10px; top: 7px; font-size: 7.2px; font-weight: 500; color: var(--brand-blue); }
  .rank-card .rank-place { position: absolute; right: 9px; top: 24px; font-size: 16.5px; font-weight: 600; line-height: 18px; }
  .rank-card .rank-of { position: absolute; right: 9px; top: 43px; font-size: 11px; font-weight: 600; color: var(--brand-blue); }
  .panel { position: absolute; left: 9px; width: 216px; background: var(--white); border-radius: 8px; }
  .panel-title { position: absolute; left: 10px; top: 9px; font-size: 7.4px; font-weight: 500; color: var(--brand-blue); }
  .stat-chip {
    position: absolute; width: 62px; height: 29px; border-radius: 15px; background: var(--chip-blue);
    display: flex; align-items: center; justify-content: center; font-size: 9.6px; font-weight: 500;
  }
</style>
</head>
<body>

<!-- Sign up screen -->
<section class="screen screen--signup" aria-label="Create account screen">
  <h1 class="abs center-x brand-title">QUORVANE</h1>
  <p class="abs center-x brand-tagline">Learn letters and words</p>
  <h2 class="abs center-x signup-heading">Create an account</h2>
  <p class="abs center-x signup-sub">Enter your email to sign up for this app</p>
  <div class="pill email-field">email@inbox.com</div>
  <div class="pill continue-btn">Continue</div>
  <div class="abs divider">or continue with</div>
  <div class="pill provider-btn"><span class="provider-dot"></span><span>Sign in with Brindlewave</span></div>
  <p class="abs center-x legal">by clicking continue, you agree to our<br><strong>Terms of service</strong> and <strong>Privet Policy</strong></p>
</section>

<!-- Main drawing screen -->
<section class="screen screen--main" aria-label="Main drawing screen">
  <div class="abs main-hero"></div>
  <svg class="abs menu-icon" width="12" height="11" viewBox="0 0 12 11"><g stroke="#fff" stroke-width="1.2" stroke-linecap="round"><line x1="1" y1="1.5" x2="11" y2="1.5"/><line x1="1" y1="5.5" x2="11" y2="5.5"/><line x1="1" y1="9.5" x2="8" y2="9.5"/></g></svg>
  <div class="abs center-x header-title">QUORVANE</div>
  <div class="abs points-pill"><span class="coin"></span>16 Points</div>
  <div class="abs draw-pad">
    <svg class="abs pen-icon" width="16" height="16" viewBox="0 0 16 16"><path d="M3 13 L4 9 L11 2 L14 5 L7 12 Z" fill="#6fa2f0"/><path d="M11 2 L14 5" stroke="#0567f5" stroke-width="1.5"/></svg>
  </div>
  <div class="abs mode-toggle"><span>Show all words</span><span class="is-active">Play all words</span></div>
  <div class="chip" style="left:13px;top:363px">word</div>
  <div class="chip" style="left:84px;top:363px">read</div>
  <div class="chip" style="left:155px;top:363px">eat</div>
  <div class="chip" style="left:13px;top:403px">dog</div>
  <div class="chip" style="left:84px;top:403px">cat</div>
  <div class="chip" style="left:155px;top:403px">door</div>
  <div class="dark-btn result-btn">Show more the result</div>
</section>

<!-- Profile screen -->
<section class="screen screen--profile" aria-label="Profile screen">
  <svg class="abs profile-band" width="234" height="150" viewBox="0 0 234 150">
    <rect width="234" height="150" fill="#0567f5"/>
    <path d="M0 91 C60 86 120 82 165 98 C195 108 220 126 234 143 L234 150 L0 150 Z" fill="#eef1f6"/>
  </svg>
  <svg class="abs icon-back" width="14" height="10" viewBox="0 0 14 10"><path d="M13 5 H1 M5 1 L1 5 L5 9" fill="none" stroke="#fff" stroke-width="1.2" stroke-linecap="round" stroke-linejoin="round"/></svg>
  <div class="abs center-x header-title" style="font-weight:500">Profile</div>
  <div class="abs avatar-large" role="img" aria-label="Profile photo of the user"></div>
  <div class="dark-btn edit-btn">Edit profile image</div>

  <div class="field-row" style="top:180px"><span class="label">Name</span><span class="value">Mira Solen</span><svg width="7" height="10" viewBox="0 0 7 10"><path d="M1 1 L5.5 5 L1 9" fill="none" stroke="#3a3f47" stroke-width="1.1"/></svg></div>
  <div class="field-row" style="top:222px"><span class="label">Username</span><span class="value">@username</span><svg width="7" height="10" viewBox="0 0 7 10"><path d="M1 1 L5.5 5 L1 9" fill="none" stroke="#3a3f47" stroke-width="1.1"/></svg></div>
  <div class="field-row" style="top:264px"><span class="label">Email</span><span class="value">name@domain</span><svg width="7" height="10" viewBox="0 0 7 10"><path d="M1 1 L5.5 5 L1 9" fill="none" stroke="#3a3f47" stroke-width="1.1"/></svg></div>
  <div class="field-row" style="top:306px"><span class="label">Bio</span><span class="value">Lorem ipsum is a...</span><svg width="7" height="10" viewBox="0 0 7 10"><path d="M1 1 L5.5 5 L1 9" fill="none" stroke="#3a3f47" stroke-width="1.1"/></svg></div>
  <div class="field-row" style="top:348px"><span class="label">Web/Links</span><span class="value">website.com</span><svg width="7" height="10" viewBox="0 0 7 10"><path d="M1 1 L5.5 5 L1 9" fill="none" stroke="#3a3f47" stroke-width="1.1"/></svg></div>
  <div class="field-row" style="top:390px"><span class="label">Web/Links</span><span class="value">website.com</span><svg width="7" height="10" viewBox="0 0 7 10"><path d="M1 1 L5.5 5 L1 9" fill="none" stroke="#3a3f47" stroke-width="1.1"/></svg></div>
  <div class="add-link"><svg width="11" height="11" viewBox="0 0 11 11"><path d="M5.5 0.5 V10.5 M0.5 5.5 H10.5" stroke="#0567f5" stroke-width="1.2"/></svg>add new web/link</div>
</section>

<!-- Stats screen -->
<section class="screen screen--stats" aria-label="QuorTally statistics screen">
  <div class="abs stats-header"></div>
  <svg class="abs icon-back" width="14" height="10" viewBox="0 0 14 10"><path d="M13 5 H1 M5 1 L1 5 L5 9" fill="none" stroke="#fff" stroke-width="1.2" stroke-linecap="round" stroke-linejoin="round"/></svg>
  <div class="abs center-x stats-title">QuorTally</div>
  <div class="abs avatar-small" role="img" aria-label="Small profile photo of the user"></div>

  <div class="tab is-active" style="left:13px;width:43px">Ranking</div>
  <div class="tab" style="left:64px;width:65px">Correct Words</div>
  <div class="tab" style="left:137px;width:60px">Today words</div>

  <div class="rank-card" style="left:9px;width:118px">
    <span class="rank-label">Total Ranking</span>
    <svg class="abs" style="left:6px;top:40px" width="20" height="18" viewBox="0 0 20 18"><path d="M5 1 H15 V6 C15 9 12.5 11 10 11 C7.5 11 5 9 5 6 Z" fill="#f5b400"/><path d="M5 3 H2 C2 6 3.5 7.5 5.5 7.5 M15 3 H18 C18 6 16.5 7.5 14.5 7.5" fill="none" stroke="#f5b400" stroke-width="1.4"/><rect x="9" y="11" width="2" height="3" fill="#f5b400"/><rect x="6" y="14" width="8" height="3" rx="1" fill="#e09a00"/></svg>
    <span class="rank-place">1st Place</span>
    <span class="rank-of">of 100</span>
  </div>
  <div class="rank-card" style="left:141px;width:130px">
    <span class="rank-label">Daily Ranking</span>
    <span class="rank-place" style="left:19px;right:auto">10st Place</span>
    <span class="rank-of" style="left:65px;right:auto">of 100</span>
  </div>

  <div class="panel" style="top:183px;height:195px">
    <span class="panel-title">Learning curve</span>
    <svg class="abs" style="left:0;top:0" width="216" height="195" viewBox="0 0 216 195">
      <g stroke="#dde1e7" stroke-width="0.6">
        <line x1="10" y1="35.5" x2="204" y2="35.5"/><line x1="10" y1="53" x2="204" y2="53"/>
        <line x1="10" y1="70" x2="204" y2="70"/><line x1="10" y1="88" x2="204" y2="88"/>
        <line x1="10" y1="105" x2="204" y2="105"/><line x1="10" y1="122" x2="204" y2="122"/>
        <line x1="10" y1="140" x2="204" y2="140"/><line x1="10" y1="157" x2="204" y2="157"/>
      </g>
      <g font-family="Inter, sans-serif" font-size="4.6" fill="#3a3f47">
        <text x="10" y="42">100 words per day</text>
        <text x="10" y="59">50 words per day</text>
      </g>
      <path d="M9 167 C20 168 30 167 36 163 C42 158 43 150 49 150 C58 149 70 150 77 147 C86 143 88 132 94 126 C98 120 102 116 108 116 C118 116 124 116 129 111 C136 104 137 92 141 80 C145 68 148 62 156 61 C164 60 170 58 176 53 C184 47 190 41 195 35" fill="none" stroke="#1aa12b" stroke-width="1.8" stroke-linecap="round"/>
      <g font-family="Inter, sans-serif" font-size="5.4" fill="#3a3f47" text-anchor="middle">
        <text x="19" y="182">Nov 23</text><text x="45" y="182">24</text><text x="71" y="182">25</text><text x="97" y="182">26</text>
        <text x="123" y="182">27</text><text x="149" y="182">28</text><text x="175" y="182">29</text><text x="201" y="182">30</text>
      </g>
    </svg>
  </div>

  <div class="panel" style="top:394px;height:130px">
    <span class="panel-title">Recently learned words</span>
  </div>
  <div class="stat-chip" style="left:19px;top:424px">word</div>
  <div class="stat-chip" style="left:87px;top:424px">read</div>
  <div class="stat-chip" style="left:156px;top:424px">eat</div>
  <div class="stat-chip" style="left:19px;top:463px">dog</div>
  <div class="stat-chip" style="left:87px;top:463px">cat</div>
  <div class="stat-chip" style="left:156px;top:463px">door</div>
</section>

</body>
</html>
```